New Construction company looking for powerful bold logo. people see the logo, leaves an impression

We need a business card for our new company. We provide site work for commercial projects in South Texas. We clear land, excavation, run under ground utilities, concrete work, dirt work etc. We like the black card. I created a webpage www.vantaridgebuilders.com .... As I grow with projects I will put up pictures with video, and intro music. Want it look cool, bold, powerful, and slick looking. Creating 'VRB'....as my logo (possibly or if you have something you want to have fun with). Just have fun!!....thank you!

Dorian Pelt Business Manager Serving South Texas PO Box 4738 Calloway Springs,TX. 78391 Mobile: 361-555-0172 www.vantaridgebuilders.com dorian@vantaridgebuilders.com you can put this anyway you see fit in your design and layout. thank you

Target Market(s)

General Contractors; Home Builders;

Industry/Entity Type

Construction

Contact Information for Business Card

I want the card to be black.

Font styles to use
Other font styles liked:
• Designer choice

Requirements
Must have
• Vanta Ridge Construction
• Site Work - Utilities/Concrete/Pad/Grading/Excavation (on the back side)
Nice to have
• Maybe VRB as the logo.....or just a symbol that would be VR.....and then construction to tie it togther...

```html
<!DOCTYPE html>
<html lang="en">
<head>
<meta charset="utf-8">
<title>Vanta Ridge Construction – Business Card</title>
<link href="https://fonts.googleapis.com/css2?family=Raleway:wght@400;500;700;800&display=swap" rel="stylesheet">
<style>
  :root {
    --ink: #0d0b18;
    --gold: #fcc600;
    --white: #ffffff;
    --stage: #d9d6d0;
  }
  * { margin: 0; padding: 0; box-sizing: border-box; }
  html, body { width: 1200px; height: 900px; overflow: hidden; }
  body {
    background: var(--stage);
    font-family: "Raleway", sans-serif;
    position: relative;
  }
  .card {
    position: absolute;
    left: 280px;
    width: 640px;
    height: 366px;
    background: var(--ink);
    overflow: hidden;
    box-shadow: 0 8px 24px rgba(0,0,0,.25);
  }
  .card--front { top: 60px; }
  .card--back { top: 470px; }
  .card__art { position: absolute; inset: 0; }

  .holder { position: absolute; left: 30px; top: 24px; }
  .holder__name {
    color: var(--gold); font-size: 34px; font-weight: 500;
    letter-spacing: 1px; line-height: 1; text-transform: uppercase;
  }
  .holder__role { color: var(--white); font-size: 19px; font-weight: 400; margin-top: 1px; letter-spacing: .3px; }

  .brand { position: absolute; display: flex; align-items: center; }
  .brand__dot { border-radius: 50%; background: var(--gold); flex: none; }
  .brand__name { color: var(--white); font-weight: 700; line-height: 1.05; text-transform: uppercase; }
  .brand--small { left: 390px; top: 30px; }
  .brand--small .brand__dot { width: 40px; height: 40px; margin-right: 12px; }
  .brand--small .brand__name { font-size: 15px; letter-spacing: .5px; }

  .services {
    position: absolute; left: 20px; top: 97px;
    color: var(--ink); font-size: 20px; font-weight: 500; white-space: nowrap;
  }
  .address {
    position: absolute; left: 30px; top: 158px;
    color: var(--white); font-size: 16px; line-height: 1.35; font-style: normal;
    letter-spacing: .3px;
  }
  .contact {
    position: absolute; right: 20px; top: 232px;
    list-style: none; text-align: right;
  }
  .contact__item {
    display: flex; justify-content: flex-end; align-items: center;
    color: var(--ink); font-size: 22px; font-weight: 400; line-height: 1.35;
  }
  .contact__icon {
    width: 20px; height: 20px; margin-left: 8px; border-radius: 50%;
    background: var(--ink); display: inline-flex; align-items: center; justify-content: center;
  }

  .brand--large { left: 96px; top: 76px; }
  .brand--large .brand__dot { width: 160px; height: 160px; margin-right: 26px; }
  .brand--large .brand__name { font-size: 40px; }
  .brand--large .brand__name span { display: block; }
  .website {
    position: absolute; left: 0; right: 0; top: 292px; text-align: center;
    color: var(--white); font-size: 30px; font-weight: 400;
  }
  .website__domain { color: var(--gold); }
</style>
</head>
<body>

<section class="card card--front" aria-label="Business card front">
  <svg class="card__art" viewBox="0 0 640 366" aria-hidden="true">
    <path d="M0,344 C240,300 470,190 640,40 L640,366 L0,366 Z" fill="var(--gold)"/>
    <path d="M0,344 C240,300 470,190 640,40" fill="none" stroke="var(--white)" stroke-width="7"/>
    <polygon points="0,94 540,94 640,26 640,58 585,126 0,126" fill="var(--white)"/>
  </svg>

  <div class="holder">
    <p class="holder__name">Dorian Pelt</p>
    <p class="holder__role">Business Manager</p>
  </div>

  <div class="brand brand--small">
    <span class="brand__dot"></span>
    <p class="brand__name">Vanta Ridge<br>Construction</p>
  </div>

  <p class="services">Site Work · Utilities · Concrete · Pad · Grading · Excavation</p>

  <address class="address">
    Serving South Texas<br>
    PO Box 4738<br>
    Calloway Springs,TX. 78391
  </address>

  <ul class="contact">
    <li class="contact__item">361-555-0172
      <span class="contact__icon"><svg width="10" height="12" viewBox="0 0 10 12"><rect x="1" y="0.5" width="8" height="11" rx="1.5" fill="none" stroke="var(--gold)" stroke-width="1.4"/></svg></span>
    </li>
    <li class="contact__item">www.vantaridgebuilders.com
      <span class="contact__icon"><svg width="12" height="12" viewBox="0 0 12 12"><circle cx="6" cy="6" r="5" fill="none" stroke="var(--gold)" stroke-width="1.2"/><path d="M1,6 H11 M6,1 V11" stroke="var(--gold)" stroke-width="1"/></svg></span>
    </li>
    <li class="contact__item">dorian@vantaridgebuilders.com
      <span class="contact__icon"><svg width="12" height="10" viewBox="0 0 12 10"><rect x="1" y="1" width="10" height="8" fill="none" stroke="var(--gold)" stroke-width="1.2"/><path d="M1,1 L6,5.5 L11,1" fill="none" stroke="var(--gold)" stroke-width="1.2"/></svg></span>
    </li>
  </ul>
</section>

<section class="card card--back" aria-label="Business card back">
  <div class="brand brand--large">
    <span class="brand__dot"></span>
    <p class="brand__name"><span>Vanta Ridge</span><span>Construction</span></p>
  </div>
  <p class="website">www.<span class="website__domain">vantaridgebuilders</span>.com</p>
</section>

</body>
</html>
```